Broschüre für Beratung von Versicherungsprodukten
Zielgruppe
Beratung von Versicherungsprodukten für Privatpersonen. Zielgruppe 20-45 männlich und weiblich.
Aufgabenstellung
Gemäss Broschüre welche eingescannt wurde. Im Prinzip das gleiche aber mit anderen Bildern und Symbolen. Bitte die jeweiligen Korrekturen vornehmen. Broschüre wenn möglich in den Farben des Logos halten. Auf der letzten Seite ganz unten nur Name und Adresse angeben, aber keine Mailadresse und www.Adresse.

```html
<!DOCTYPE html>
<html lang="de">
<head>
<meta charset="utf-8">
<title>Kundendaten – Beratungsbroschüre</title>
<link href="https://fonts.googleapis.com/css2?family=Questrial&display=swap" rel="stylesheet">
<style>
  :root{
    --bg:#ecebe8;
    --paper:#ffffff;
    --blue:#2b5fa9;
    --teal:#7cbdae;
    --teal-dark:#4fa794;
    --green-light:#dcefe4;
    --slate:#5b6898;
    --slate-light:#c9cbe0;
    --grey-light:#e8eaeb;
    --ink:#4b5566;
    --ink-soft:#8a93a0;
    --line:#b9c3d6;
    --yellow:#f5ef8c;
    --red:#d6392a;
    --green:#abd5a3;
    --font:"Questrial", "Helvetica Neue", Arial, sans-serif;
  }
  *{box-sizing:border-box;margin:0;padding:0}
  html,body{width:1200px;height:800px;overflow:hidden;background:var(--bg)}
  .canvas{position:relative;width:1200px;height:800px;overflow:hidden;font-family:var(--font);color:var(--ink)}
  .sheet{position:absolute;background:var(--paper);box-shadow:0 1px 4px rgba(0,0,0,.18)}
  .sheet svg{display:block;width:100%;height:100%}
  svg text{font-family:var(--font);fill:var(--ink)}
  .band{fill:var(--blue)}
  .band-title{fill:#fff;font-size:5px}
  .brand{fill:var(--blue);font-size:3.2px}
  .h{font-size:4.6px;fill:var(--ink)}
  .h-blue{font-size:4.6px;fill:var(--blue)}
  .lbl{font-size:2.5px;fill:var(--ink)}
  .lbl-w{font-size:2.6px;fill:#fff}
  .ln{stroke:var(--line);stroke-width:.4;fill:none}
  .fold{stroke:#e3e5e8;stroke-width:.5}
  .box-teal{fill:var(--teal)}
  .box-green{fill:var(--green-light)}
  .box-grey{fill:var(--grey-light)}
  .box-slate{fill:var(--slate)}
  .box-slate-l{fill:var(--slate-light)}
  .chk{fill:none;stroke:var(--ink-soft);stroke-width:.35}
</style>
</head>
<body>
<div class="canvas">

<svg width="0" height="0" style="position:absolute" aria-hidden="true">
  <defs>
    <symbol id="band" viewBox="0 0 110 26" preserveAspectRatio="none">
      <path d="M0 6 C40 0 86 2 110 25 C76 15 36 17 0 24 Z"/>
    </symbol>
    <linearGradient id="sky" x1="0" y1="0" x2="0" y2="1">
      <stop offset="0" stop-color="#6f9fd6"/>
      <stop offset=".55" stop-color="#dfe9f4"/>
      <stop offset="1" stop-color="#9fb0bf"/>
    </linearGradient>
    <linearGradient id="door" x1="0" y1="0" x2="1" y2="0">
      <stop offset="0" stop-color="#8a3a22"/>
      <stop offset=".55" stop-color="#c9a48c"/>
      <stop offset="1" stop-color="#e6e1db"/>
    </linearGradient>
    <linearGradient id="gap" x1="0" y1="0" x2="0" y2="1">
      <stop offset="0" stop-color="#c8221a"/>
      <stop offset="1" stop-color="#f0a090"/>
    </linearGradient>
    <pattern id="grid" width="4" height="4" patternUnits="userSpaceOnUse">
      <path d="M4 0 H0 V4" fill="none" stroke="#d6d9de" stroke-width=".3"/>
    </pattern>
  </defs>
</svg>

<!-- Cover -->
<div class="sheet cover" style="left:24px;top:23px;width:191px;height:270px">
  <svg viewBox="0 0 191 270">
    <circle cx="46" cy="48" r="3" fill="var(--teal-dark)"/>
    <text x="52" y="51" style="font-size:9px;fill:var(--blue)">Nordlicht Vorsorge</text>
    <text x="95.5" y="60" text-anchor="middle" style="font-size:3.6px;fill:var(--teal-dark)">Wir begleiten Sie auf Ihrem Weg</text>
    <rect x="0" y="66" width="191" height="124" fill="url(#sky)" role="img" aria-label="Foto: Holzsteg ins Meer unter Wolkenhimmel mit hellen Versicherungssymbolen"/>
    <path d="M0 192 C60 176 130 176 191 182 L191 205 C130 203 60 212 0 232 Z" class="band"/>
    <text x="30" y="207" style="font-size:10px;fill:#fff">Kundendaten</text>
    <rect x="20" y="214" width="110" height="56" class="box-green"/>
    <text x="27" y="237" class="lbl">Kunde</text>
    <text x="27" y="255" class="lbl">Termin</text>
    <path d="M27 234 H122 M27 252 H122" class="ln"/>
  </svg>
</div>

<!-- Personal data / health -->
<div class="sheet spread" style="left:233px;top:23px;width:381px;height:270px">
  <svg viewBox="0 0 381 270">
    <line x1="190" y1="0" x2="190" y2="270" class="fold"/>
    <use href="#band" x="0" y="8" width="100" height="24" class="band"/>
    <text x="19" y="18.5" class="band-title">Meine persönlichen Daten</text>
    <text x="117" y="19" class="lbl">Datum</text>
    <path d="M127 19 H172" class="ln"/>

    <text x="44" y="84" class="h">Kunde</text>
    <text x="110" y="84" class="h">Partner</text>
    <g text-anchor="end">
      <text x="41" y="90" class="lbl">Vorname</text>
      <text x="41" y="96" class="lbl">Name</text>
      <text x="41" y="102" class="lbl">Adresse</text>
      <text x="41" y="108" class="lbl">PLZ/Ort</text>
      <text x="41" y="114" class="lbl">Telefon / Mobil</text>
      <text x="41" y="120" class="lbl">E-Mail</text>
      <text x="41" y="126" class="lbl">Geburtsdatum</text>
      <text x="41" y="132" class="lbl">Nationalität</text>
      <text x="41" y="138" class="lbl">Aufenthaltsbewilligung</text>
      <text x="41" y="144" class="lbl">Zivilstand</text>
      <text x="41" y="168" class="lbl">Tätigkeit</text>
    </g>
    <path class="ln" d="M44 90 H104 M108 90 H172 M44 96 H104 M108 96 H172 M44 102 H104 M108 102 H172 M44 108 H104 M108 108 H172 M44 114 H104 M108 114 H172 M44 120 H104 M108 120 H172 M44 126 H104 M108 126 H172 M44 132 H104 M108 132 H172 M44 138 H104 M108 138 H172 M44 168 H104 M108 168 H172"/>
    <g class="chk">
      <rect x="44" y="142" width="2" height="2"/><rect x="44" y="147" width="2" height="2"/><rect x="44" y="152" width="2" height="2"/>
      <rect x="82" y="142" width="2" height="2"/><rect x="82" y="147" width="2" height="2"/><rect x="82" y="152" width="2" height="2"/>
      <rect x="108" y="142" width="2" height="2"/><rect x="108" y="147" width="2" height="2"/><rect x="108" y="152" width="2" height="2"/>
      <rect x="146" y="142" width="2" height="2"/><rect x="146" y="147" width="2" height="2"/><rect x="146" y="152" width="2" height="2"/>
    </g>
    <g class="lbl">
      <text x="47.5" y="144">ledig</text><text x="47.5" y="149">verheiratet</text><text x="47.5" y="154">eingetragene Partnerschaft</text>
      <text x="85.5" y="144">Konkubinat</text><text x="85.5" y="149">geschieden</text><text x="85.5" y="154">verwitwet</text>
      <text x="111.5" y="144">ledig</text><text x="111.5" y="149">verheiratet</text><text x="111.5" y="154">eingetragene Partnerschaft</text>
      <text x="149.5" y="144">Konkubinat</text><text x="149.5" y="149">geschieden</text><text x="149.5" y="154">verwitwet</text>
    </g>

    <text x="44" y="192" class="h">Kinder</text>
    <g text-anchor="end">
      <text x="41" y="198" class="lbl">Name / Vorname</text><text x="41" y="204" class="lbl">Geburtsdatum</text>
      <text x="41" y="214" class="lbl">Name / Vorname</text><text x="41" y="220" class="lbl">Geburtsdatum</text>
      <text x="41" y="230" class="lbl">Name / Vorname</text><text x="41" y="236" class="lbl">Geburtsdatum</text>
      <text x="41" y="246" class="lbl">Name / Vorname</text><text x="41" y="252" class="lbl">Geburtsdatum</text>
    </g>
    <path class="ln" d="M44 198 H106 M44 204 H106 M44 214 H106 M44 220 H106 M44 230 H106 M44 236 H106 M44 246 H106 M44 252 H106"/>
    <circle cx="10" cy="258" r="2" fill="var(--teal-dark)"/>
    <text x="13.5" y="259" class="brand">Nordlicht Vorsorge</text>

    <use href="#band" x="0" y="8" width="100" height="24" class="band" transform="translate(381 0) scale(-1 1)"/>
    <text x="329" y="18.5" class="band-title">Meine Gesundheit</text>

    <rect x="259" y="51" width="54" height="20" class="box-teal"/>
    <text x="286" y="57" text-anchor="middle" class="lbl-w">KVG</text>
    <text x="286" y="61" text-anchor="middle" class="lbl-w">obligatorisch</text>
    <text x="286" y="65" text-anchor="middle" class="lbl-w">• Unfalldeckung</text>
    <g class="box-teal">
      <rect x="213" y="75" width="31" height="8"/><rect x="248" y="75" width="31" height="8"/><rect x="283" y="75" width="31" height="8"/><rect x="318" y="75" width="31" height="8"/>
      <rect x="213" y="89" width="20" height="11"/><rect x="236" y="89" width="20" height="11"/><rect x="259" y="89" width="20" height="11"/><rect x="282" y="89" width="20" height="11"/><rect x="305" y="89" width="20" height="11"/><rect x="328" y="89" width="20" height="11"/>
    </g>
    <g class="lbl-w">
      <text x="216" y="80">• freie Arztwahl</text><text x="251" y="80">• Hausarzt</text><text x="286" y="80">• HMO</text><text x="321" y="80">• Telmed</text>
      <text x="216" y="95.5">• 300.-</text><text x="239" y="95.5">• 500.-</text><text x="262" y="95.5">• 1'000.-</text><text x="285" y="95.5">• 1'500.-</text><text x="308" y="95.5">• 2'000.-</text><text x="331" y="95.5">• 2'500.-</text>
    </g>
    <rect x="259" y="116" width="45" height="20" class="box-teal"/>
    <text x="281.5" y="124" text-anchor="middle" class="lbl-w">VVG</text>
    <text x="281.5" y="129" text-anchor="middle" class="lbl-w">Zusatzversicherung</text>
    <g class="box-teal">
      <rect x="213" y="140" width="43" height="31"/><rect x="259" y="140" width="44" height="31"/><rect x="306" y="140" width="43" height="31"/>
      <rect x="213" y="180" width="136" height="71"/>
    </g>
    <g class="lbl-w">
      <text x="216" y="145">• Ambulant</text><text x="262" y="145">• Spitalzusatz</text><text x="309" y="145">• Alternativmedizin</text>
      <text x="216" y="153">Transportkosten</text><text x="216" y="157">Nichtkassenmedikamente</text><text x="216" y="161">Prävention</text><text x="216" y="165">Fitness / Sehhilfen</text>
      <text x="262" y="153">Allgemein</text><text x="262" y="157">Halbprivat</text><text x="262" y="161">Privat</text>
      <text x="309" y="153">Osteopathie</text><text x="309" y="157">Massagen</text><text x="309" y="161">Heilkräuter</text><text x="309" y="165">Akupunktur</text>
      <text x="216" y="186" style="font-size:3px">Weitere Zusatzdeckungen</text>
      <text x="216" y="194">• Auslandschutz / Auslandreisen (Behandlung bei Arzt/Spital)</text>
      <text x="216" y="199">• Aufbesserung Unfallversicherung (z.B. private Spitaldeckung)</text>
      <text x="216" y="204">• Rechtsschutz (Allgemein, Gesundheit, Verkehr)</text>
      <text x="216" y="209">• Taggeldversicherung</text>
      <text x="222" y="214">Höhe Unfalltaggeld CHF ________  Wartefrist Tage ________</text>
      <text x="222" y="219">Höhe Krankentaggeld CHF ________  Wartefrist Tage ________</text>
      <text x="216" y="229">• Kapitalversicherung</text>
      <text x="222" y="234">Höhe Invaliditätskapital CHF ______________</text>
      <text x="222" y="239">Höhe Todesfallkapital CHF ______________</text>
    </g>
    <circle cx="345" cy="258" r="2" fill="var(--teal-dark)"/>
    <text x="348.5" y="259" class="brand">Nordlicht Vorsorge</text>
  </svg>
</div>

<!-- Retirement / notes -->
<div class="sheet spread" style="left:632px;top:23px;width:383px;height:270px">
  <svg viewBox="0 0 383 270">
    <line x1="191" y1="0" x2="191" y2="270" class="fold"/>
    <use href="#band" x="0" y="8" width="100" height="24" class="band"/>
    <text x="19" y="18.5" class="band-title">Nordlicht Vorsorge</text>

    <text x="34" y="46" class="h">Einkommen absichern</text>
    <g class="lbl" text-anchor="end"><text x="34" y="58">100%</text><text x="34" y="67">80%</text><text x="34" y="76">60%</text></g>
    <path d="M38 52 V102 H172" class="ln"/>
    <rect x="62" y="57" width="10" height="45" fill="#bfe0d8"/>
    <rect x="72" y="67" width="30" height="35" class="box-teal"/>
    <text x="87" y="86" text-anchor="middle" class="lbl-w">Krankentaggeld</text>
    <rect x="102" y="67" width="70" height="8" fill="url(#gap)"/>
    <rect x="102" y="75" width="70" height="12" fill="var(--yellow)"/>
    <rect x="102" y="87" width="70" height="15" fill="var(--green)"/>
    <text x="128" y="83" class="lbl">BVG-Leistungen</text>
    <text x="112" y="97" class="lbl">IV-Rente</text><text x="152" y="97" class="lbl">AHV</text>
    <g class="lbl"><text x="50" y="108">Eintritt Erwerbsunfähigkeit</text><text x="102" y="108">2 Jahre</text><text x="140" y="108">Pensionierung</text></g>

    <text x="34" y="118" class="h">Hinterlassene schützen</text>
    <g class="lbl" text-anchor="end"><text x="34" y="130">100%</text><text x="34" y="139">80%</text><text x="34" y="148">60%</text></g>
    <path d="M38 124 V174 H172" class="ln"/>
    <rect x="62" y="137" width="110" height="8" fill="url(#gap)"/>
    <rect x="62" y="145" width="110" height="10" fill="var(--yellow)"/>
    <rect x="62" y="155" width="110" height="19" fill="var(--green)"/>
    <text x="70" y="152" class="lbl">Hinterlassenenrente</text>
    <text x="70" y="166" class="lbl">AHV-Hinterlassenenrente</text><text x="152" y="166" class="lbl">AHV</text>
    <g class="lbl"><text x="62" y="180">Tod</text><text x="140" y="180">Pensionierung</text></g>

    <text x="34" y="192" class="h">Sorglos im Alter</text>
    <g class="lbl" text-anchor="end"><text x="34" y="204">100%</text><text x="34" y="213">80%</text><text x="34" y="222">60%</text></g>
    <path d="M38 198 V248 H172" class="ln"/>
    <rect x="62" y="215" width="110" height="9" fill="url(#gap)"/>
    <rect x="62" y="224" width="110" height="10" fill="var(--yellow)"/>
    <rect x="62" y="234" width="110" height="14" fill="var(--green)"/>
    <text x="70" y="230" class="lbl">BVG-Renten</text><text x="70" y="242" class="lbl">AHV-Rente</text><text x="100" y="242" class="lbl">AHV gesplittet</text>
    <circle cx="10" cy="258" r="2" fill="var(--teal-dark)"/>
    <text x="13.5" y="259" class="brand">Nordlicht Vorsorge</text>

    <use href="#band" x="0" y="8" width="100" height="24" class="band" transform="translate(383 0) scale(-1 1)"/>
    <text x="342" y="18.5" class="band-title">Notizen</text>
    <rect x="203" y="37" width="168" height="220" fill="url(#grid)" stroke="#d6d9de" stroke-width=".3"/>
  </svg>
</div>

<!-- Mobility -->
<div class="sheet spread" style="left:810px;top:209px;width:375px;height:265px">
  <svg viewBox="0 0 375 265">
    <line x1="187.5" y1="0" x2="187.5" y2="265" class="fold"/>
    <use href="#band" x="0" y="8" width="100" height="24" class="band"/>
    <text x="19" y="18.5" class="band-title">Sicher mobil</text>

    <circle cx="49" cy="71" r="30" fill="none" stroke="var(--blue)" stroke-width="2.5" stroke-dasharray="120 68"/>
    <circle cx="49" cy="71" r="23" fill="none" stroke="var(--teal)" stroke-width="9" stroke-dasharray="16 2"/>
    <circle cx="49" cy="71" r="16" fill="var(--grey-light)"/>
    <circle cx="49" cy="71" r="7" fill="#fff" stroke="var(--blue)" stroke-width=".6"/>

    <text x="22" y="117" class="lbl" style="font-size:3px">Motorrad</text>
    <text x="30" y="123" class="lbl">Schutzbekleidung im Wert von CHF</text>
    <text x="30" y="128" class="lbl">○ 2000.-   ○ 4000.-</text>
    <text x="22" y="143" class="lbl" style="font-size:3px">Allgemeine Optionen</text>
    <text x="22" y="149" class="lbl">○ Bonusschutz auf allen Prämienstufen</text>
    <text x="22" y="155" class="lbl">○ Regressverzicht bei Grobfahrlässigkeit</text>
    <text x="22" y="163" class="lbl">○ Assistance Pannenhilfe</text>
    <rect x="21" y="170" width="64" height="56" class="box-grey"/>
    <text x="24" y="176" class="lbl" style="font-size:3px">Optionen Kaskoversicherung</text>
    <text x="24" y="182" class="lbl">○ Erweiterte Glasdeckung</text>
    <text x="24" y="189" class="lbl">Mitgeführte Sachen CHF</text>
    <text x="24" y="194" class="lbl">○ 2000.- ○ 3000.- ○ 4000.-</text>
    <text x="24" y="202" class="lbl">Parkschaden</text>
    <text x="24" y="207" class="lbl">○ Unbegrenzte Deckung</text>
    <text x="24" y="215" class="lbl">○ Unbegrenzte Deckung</text>

    <rect x="107" y="9" width="61" height="57" class="box-grey"/>
    <text x="110" y="15" class="lbl" style="fill:var(--teal-dark)">Haftpflicht</text>
    <text x="118" y="23" class="lbl">Schadenersatzansprüche</text>
    <text x="118" y="27" class="lbl">für Personen- und Sachschäden</text>
    <text x="118" y="40" class="lbl">Abwehr von unberechtigten</text>
    <text x="118" y="44" class="lbl">Ansprüchen</text>
    <text x="118" y="55" class="lbl">CHF 100 Mio. Deckungssumme</text>
    <text x="110" y="63" class="lbl">Selbstbehalt CHF ○ 0.- ○ 300.- ○ 500.-</text>
    <path d="M107 70 H168 V164 L137.5 176 L107 164 Z" class="box-green"/>
    <text x="110" y="76" class="lbl" style="fill:var(--teal-dark)">Teilkasko</text>
    <g class="lbl">
      <text x="118" y="84">Feuer</text><text x="118" y="92">Glasbruch</text><text x="118" y="100">Diebstahl</text><text x="118" y="108">Kollision mit Tieren</text>
      <text x="118" y="116">Vandalenschäden</text><text x="118" y="124">Marderschäden</text><text x="118" y="132">Hilfeleistungen</text><text x="118" y="140">Schneerutsch</text><text x="118" y="148">Elementarereignisse</text>
      <text x="110" y="158">Selbstbehalt CHF ○ 0.- ○ 300.- ○ 500.-</text>
    </g>
    <path d="M107 168 L137.5 180 L168 168 V203 H107 Z" class="box-slate"/>
    <text x="110" y="186" class="lbl-w">Vollkasko</text>
    <text x="118" y="193" class="lbl-w">Kollision</text>
    <text x="110" y="200" class="lbl-w">Selbstbehalt CHF ○ 0.- ○ 300.- ○ 500.-</text>
    <text x="107" y="212" class="lbl" style="font-size:3px">Unfallversicherung</text>
    <g class="lbl">
      <text x="107" y="218">○ Lenker und Mitfahrer</text><text x="145" y="218">Nur Mitfahrer</text>
      <text x="107" y="224">○ Heilungskosten für Haustiere</text><text x="107" y="230">○ Heilungskosten</text>
      <text x="107" y="236">○ Taggeld</text><text x="107" y="242">○ Invaliditätskapital</text><text x="107" y="248">○ Todesfallkapital</text>
    </g>
    <circle cx="10" cy="253" r="2" fill="var(--teal-dark)"/>
    <text x="13.5" y="254" class="brand">Nordlicht Vorsorge</text>

    <use href="#band" x="0" y="8" width="100" height="24" class="band" transform="translate(375 0) scale(-1 1)"/>
    <text x="330" y="18.5" class="band-title">Meine Daten</text>
    <text x="213" y="48" class="lbl" style="font-size:3px">Versicherungsnehmer/</text>
    <text x="213" y="52" class="lbl" style="font-size:3px">Fahrzeughalter</text>
    <text x="286" y="48" class="lbl" style="font-size:3px">Häufigster Lenker</text>
    <g class="lbl">
      <text x="213" y="61">Vorname</text><text x="213" y="66">Name</text><text x="213" y="71">Adresse</text><text x="213" y="76">PLZ/Ort</text><text x="213" y="81">Geburtsdatum</text><text x="213" y="86">Geschlecht ○ Mann ○ Frau</text><text x="213" y="91">Nationalität</text><text x="213" y="96">Aufenthaltsbewilligung</text><text x="213" y="101">Führerausweis seit</text><text x="213" y="106">Vorversicherer</text><text x="213" y="111">Schadenfälle ○ Vollkasko</text>
      <text x="286" y="61">Vorname</text><text x="286" y="66">Name</text><text x="286" y="71">Adresse</text><text x="286" y="76">PLZ/Ort</text><text x="286" y="81">Geburtsdatum</text><text x="286" y="86">Geschlecht ○ Mann ○ Frau</text><text x="286" y="91">Nationalität</text><text x="286" y="96">Aufenthaltsbewilligung</text><text x="286" y="101">Führerausweis seit</text><text x="286" y="106">Vorversicherer</text><text x="286" y="111">Schadenfälle ○ Vollkasko</text>
    </g>
    <path class="ln" d="M232 61 H278 M305 61 H351 M232 66 H278 M305 66 H351 M232 71 H278 M305 71 H351 M232 76 H278 M305 76 H351 M234 81 H278 M307 81 H351 M234 91 H278 M307 91 H351 M240 96 H278 M313 96 H351 M236 101 H278 M309 101 H351 M234 106 H278 M307 106 H351"/>
    <text x="213" y="146" class="lbl" style="font-size:3px">Fahrzeug 1</text>
    <text x="286" y="146" class="lbl" style="font-size:3px">Fahrzeug 2</text>
    <g class="lbl">
      <text x="213" y="155">Kontrollschild</text><text x="213" y="160">Nutzung ○ privat ○ geschäftlich</text><text x="213" y="165">Leasing ○ Ja ○ Nein</text><text x="213" y="170">Wechselschild ○ Ja ○ Nein</text><text x="213" y="175">Garage ○ Ja ○ Nein</text><text x="213" y="180">Marke / Modell</text><text x="213" y="185">Typenschein</text><text x="213" y="190">1. Inverkehrsetzung</text><text x="213" y="195">PS / Hubraum</text><text x="213" y="200">Katalogpreis / Zubehör</text><text x="213" y="205">Stammnummer</text><text x="213" y="210">Jährliche Fahrleistung</text><text x="213" y="215">Fahrzeugart</text>
      <text x="286" y="155">Kontrollschild</text><text x="286" y="160">Nutzung ○ privat ○ geschäftlich</text><text x="286" y="165">Leasing ○ Ja ○ Nein</text><text x="286" y="170">Wechselschild ○ Ja ○ Nein</text><text x="286" y="175">Garage ○ Ja ○ Nein</text><text x="286" y="180">Marke / Modell</text><text x="286" y="185">Typenschein</text><text x="286" y="190">1. Inverkehrsetzung</text><text x="286" y="195">PS / Hubraum</text><text x="286" y="200">Katalogpreis / Zubehör</text><text x="286" y="205">Stammnummer</text><text x="286" y="210">Jährliche Fahrleistung</text><text x="286" y="215">Fahrzeugart</text>
    </g>
    <path class="ln" d="M232 155 H278 M305 155 H351 M234 180 H278 M307 180 H351 M232 185 H278 M305 185 H351 M238 190 H278 M311 190 H351 M232 195 H278 M305 195 H351 M241 200 H278 M314 200 H351 M234 205 H278 M307 205 H351 M240 210 H278 M313 210 H351 M232 215 H278 M305 215 H351"/>
    <circle cx="339" cy="253" r="2" fill="var(--teal-dark)"/>
    <text x="342.5" y="254" class="brand">Nordlicht Vorsorge</text>
  </svg>
</div>

<!-- Home -->
<div class="sheet spread" style="left:160px;top:502px;width:373px;height:264px">
  <svg viewBox="0 0 373 264">
    <line x1="186.5" y1="0" x2="186.5" y2="264" class="fold"/>
    <use href="#band" x="0" y="8" width="100" height="24" class="band"/>
    <text x="19" y="18.5" class="band-title">Rundumschutz zuhause</text>
    <circle cx="54" cy="64" r="31" fill="none" stroke="var(--blue)" stroke-width="2.5" stroke-dasharray="60 40"/>
    <circle cx="54" cy="64" r="24" fill="none" stroke="var(--teal)" stroke-width="9" stroke-dasharray="18 2"/>
    <circle cx="54" cy="64" r="17" fill="var(--grey-light)"/>
    <circle cx="54" cy="64" r="7" fill="#fff" stroke="var(--blue)" stroke-width=".6"/>
    <text x="27" y="128" class="lbl" style="font-size:3px">Optionen</text>
    <g class="lbl">
      <text x="27" y="136">○ Reisegepäck</text><text x="27" y="142">○ Wertsachenversicherung</text><text x="27" y="148">○ Einfacher Diebstahl auswärts</text>
      <text x="30" y="169">Deckung ______________ CHF</text><text x="27" y="175">○ Sportgerätekasko</text><text x="30" y="181">Deckung ______________ CHF</text>
      <text x="27" y="196">○ Gebäudeglaskasko</text><text x="30" y="202">Deckung ______________ CHF</text>
      <text x="27" y="215">○ Hausrat zum Neuwert versichert</text>
    </g>
    <rect x="102" y="36" width="62" height="57" class="box-green"/>
    <text x="105" y="42" class="lbl" style="font-size:3px">Hausrat</text>
    <g class="lbl"><text x="116" y="52">Diebstahl</text><text x="116" y="63">Wasser</text><text x="116" y="74">Feuer</text><text x="116" y="86">Glasbruch</text></g>
    <rect x="102" y="98" width="62" height="49" class="box-slate-l"/>
    <text x="105" y="104" class="lbl" style="font-size:3px">Privathaftpflicht</text>
    <text x="105" y="110" class="lbl">○ Einzel   ○ Familie</text>
    <text x="115" y="118" class="lbl">Schadenersatzansprüche</text><text x="115" y="122" class="lbl">für Personen- und Sachschäden</text>
    <text x="115" y="134" class="lbl">Abwehr von unberechtigten</text><text x="115" y="138" class="lbl">Ansprüchen</text>
    <rect x="102" y="147" width="62" height="102" class="box-slate"/>
    <g class="lbl-w">
      <text x="105" y="153" style="font-size:3px">Zusatzrisiken</text>
      <text x="105" y="161">○ Standard-Lenkerdeckung</text>
      <text x="105" y="169">○ Grobfahrlässigkeit: keine</text><text x="108" y="173">Kürzung der Leistung bei</text><text x="108" y="177">grobfahrlässigem Handeln</text>
      <text x="105" y="189">○ Jagdausübung</text>
      <text x="105" y="197">○ gemietete / geliehene Pferde</text>
      <text x="105" y="205">○ Halter von Modellflugzeugen</text><text x="108" y="209">inkl. Drohnen</text>
      <text x="105" y="217">○ Gokarts / Pocket Bikes</text>
      <text x="105" y="225">○ Benützung fremder</text><text x="108" y="229">Wasserfahrzeuge</text>
    </g>
    <circle cx="10" cy="252" r="2" fill="var(--teal-dark)"/>
    <text x="13.5" y="253" class="brand">Nordlicht Vorsorge</text>

    <rect x="283" y="9" width="90" height="81" fill="url(#door)" role="img" aria-label="Foto: Paar steht lächelnd in der Haustür ihres Zuhauses"/>
    <use href="#band" x="0" y="8" width="100" height="24" class="band" transform="translate(373 0) scale(-1 1)"/>
    <text x="326" y="18.5" class="band-title">Mein Heim</text>
    <g class="lbl">
      <text x="201" y="44">○ Mehrfamilienhaus</text><text x="236" y="44">○ Einfamilienhaus</text>
      <text x="201" y="49">○ Eigentümer</text><text x="236" y="49">○ Mieter</text>
      <text x="201" y="56">Versicherungsort</text><text x="201" y="68">Versicherungssumme</text><text x="272" y="74">CHF</text>
      <text x="201" y="98" style="font-size:3px">Einrichtungsart</text>
      <text x="201" y="104">○ einfach   ○ mittel   ○ gehoben</text>
      <text x="201" y="110">Anzahl Zimmer ___  Anzahl Personen ___  ___ Erwachsene  ___ Kinder</text>
      <text x="201" y="125" style="font-size:3px">Weitere Objekte</text>
      <text x="201" y="131">○ alle eigenen Fahrräder</text><text x="201" y="137">○ Wertsachen</text><text x="201" y="143">○ Kunstobjekte</text>
      <text x="256" y="131">○ Schwimmbad, Jacuzzi</text><text x="256" y="137">○ Gartenanlage</text><text x="256" y="143">○ Ferienwohnung / Haus</text><text x="256" y="149">○ Fahrnisbauten</text>
      <text x="201" y="155">Besondere Gegenstände / Kunstobjekte</text>
      <text x="201" y="175" style="font-size:3px">Mein Heim</text>
      <text x="201" y="181">Gebäudeversicherungssumme ________ CHF  Bau- / Schätzjahr ________</text>
      <text x="201" y="187">○ Flachdach   ○ Boden-/Deckenheizung</text>
      <text x="201" y="193">Hypothekarsumme ________  Ablauf ________  Anbieter ________</text>
      <text x="201" y="209" style="font-size:3px">Frühere Schadenfälle</text>
      <text x="201" y="215">Datum</text><text x="236" y="215">Betrag</text><text x="275" y="215">Art / Risiko</text><text x="305" y="215">Hinweise</text>
    </g>
    <path class="ln" d="M201 61 H272 M201 74 H271 M201 161 H352 M201 222 H225 M236 222 H265 M275 222 H298 M305 222 H352 M201 229 H225 M236 229 H265 M275 229 H298 M305 229 H352 M201 236 H225 M236 236 H265 M275 236 H298 M305 236 H352 M201 243 H225 M236 243 H265 M275 243 H298 M305 243 H352"/>
    <circle cx="337" cy="252" r="2" fill="var(--teal-dark)"/>
    <text x="340.5" y="253" class="brand">Nordlicht Vorsorge</text>
  </svg>
</div>

<!-- Legal protection / feedback -->
<div class="sheet spread" style="left:556px;top:501px;width:377px;height:265px">
  <svg viewBox="0 0 377 265">
    <line x1="188.5" y1="0" x2="188.5" y2="265" class="fold"/>
    <use href="#band" x="0" y="8" width="100" height="28" class="band"/>
    <text x="19" y="16" class="band-title">Die Leistungen der</text>
    <text x="19" y="22" class="band-title">Rechtsschutzversicherung</text>
    <circle cx="49" cy="76" r="30" fill="none" stroke="var(--blue)" stroke-width="2.5" stroke-dasharray="70 120" transform="rotate(80 49 76)"/>
    <circle cx="49" cy="76" r="23" fill="none" stroke="var(--teal)" stroke-width="9" stroke-dasharray="16 2"/>
    <circle cx="49" cy="76" r="16" fill="var(--grey-light)"/>
    <text x="49" y="80" text-anchor="middle" style="font-size:11px;fill:var(--ink)">§</text>

    <rect x="108" y="10" width="62" height="47" class="box-green"/>
    <text x="111" y="16" class="lbl" style="fill:var(--teal-dark)">Privat</text>
    <g class="lbl"><text x="120" y="24">Arbeitsvertragliche Streitigkeiten</text><text x="120" y="31">Mietvertragliche Streitigkeiten</text><text x="120" y="38">Kaufvertragliche Streitigkeiten</text><text x="120" y="45">...und viele weitere Deckungen</text></g>
    <rect x="108" y="60" width="62" height="47" class="box-green"/>
    <text x="111" y="66" class="lbl" style="fill:var(--teal-dark)">Verkehr</text>
    <g class="lbl"><text x="120" y="74">Kauf eines Fahrzeugs</text><text x="120" y="81">Unterstützung bei einem Unfall</text><text x="120" y="88">Hilfe bei Ausweisentzug</text><text x="120" y="95">...und viele weitere Deckungen</text></g>
    <text x="108" y="113" class="lbl" style="font-size:3px">Optionen</text>
    <text x="108" y="120" class="lbl">○ Einzel    ○ Familie</text>

    <text x="12" y="133" class="lbl" style="font-size:3px">In diesen und weiteren Fällen sind Sie geschützt (Privat &amp; Verkehr)</text>
    <rect x="19" y="137" width="152" height="6" class="box-slate"/>
    <text x="22" y="141" class="lbl-w">Themenfeld</text><text x="56" y="141" class="lbl-w">Typischer Fall</text>
    <g class="box-slate-l">
      <rect x="19" y="145" width="152" height="6"/><rect x="19" y="161" width="152" height="6"/><rect x="19" y="177" width="152" height="6"/><rect x="19" y="193" width="152" height="6"/><rect x="19" y="209" width="152" height="6"/><rect x="19" y="225" width="152" height="6"/>
    </g>
    <path fill="none" stroke="var(--blue)" stroke-width=".8" d="M12 148 l1 1 l2 -2.5 M12 156 l1 1 l2 -2.5 M12 164 l1 1 l2 -2.5 M12 172 l1 1 l2 -2.5 M12 180 l1 1 l2 -2.5 M12 188 l1 1 l2 -2.5 M12 196 l1 1 l2 -2.5 M12 204 l1 1 l2 -2.5 M12 212 l1 1 l2 -2.5 M12 220 l1 1 l2 -2.5 M12 228 l1 1 l2 -2.5"/>
    <g class="lbl">
      <text x="22" y="149">Mietwohnung</text><text x="56" y="149">Die Nebenkostenabrechnung ist nicht korrekt</text>
      <text x="22" y="157">Kauf</text><text x="56" y="157">Der Gebrauchtwagen erweist sich als Unfallwagen</text>
      <text x="22" y="165">Gesundheit</text><text x="56" y="165">Die Operation ist misslungen</text>
      <text x="22" y="173">Versicherung</text><text x="56" y="173">Die Versicherung zahlt den Schaden nicht</text>
      <text x="22" y="181">Arbeitsvertrag</text><text x="56" y="181">Die fristlose Kündigung ist unbegründet</text>
      <text x="22" y="189">Miete</text><text x="56" y="189">Die Kosten für den Kühlschrank werden nicht übernommen</text>
      <text x="22" y="197">Baueinsprache</text><text x="56" y="197">Der Nachbar will zu nahe bauen</text>
      <text x="22" y="205">Auftragsrecht</text><text x="56" y="205">Die Reinigungskraft verrechnet zu viele Stunden</text>
      <text x="22" y="213">Stockwerkeigentum</text><text x="56" y="213">Die Heizkosten werden nicht korrekt aufgeteilt</text>
      <text x="22" y="221">Nachbarrecht</text><text x="56" y="221">Der Nachbar verursacht übermässig Lärm</text>
      <text x="22" y="229">Verkehr</text><text x="56" y="229">Die Verkehrsbusse ist ungerechtfertigt</text>
    </g>
    <circle cx="10" cy="253" r="2" fill="var(--teal-dark)"/>
    <text x="13.5" y="254" class="brand">Nordlicht Vorsorge</text>

    <use href="#band" x="0" y="6" width="100" height="24" class="band" transform="translate(377 0) scale(-1 1)"/>
    <text x="330" y="16.5" class="band-title">Mein Eindruck</text>
    <circle cx="211" cy="41" r="4" fill="none" stroke="#e05a4a" stroke-width=".8"/>
    <circle cx="248" cy="41" r="4" fill="none" stroke="#e8d84a" stroke-width=".8"/>
    <circle cx="285" cy="41" r="4" fill="none" stroke="#8cc66a" stroke-width=".8"/>
    <g class="lbl">
      <text x="216.5" y="42">○</text><text x="253.5" y="42">○</text><text x="290.5" y="42">○</text>
      <text x="205" y="63" style="font-size:3px">Zufriedenheit mit der Beratung</text>
      <text x="205" y="71">Wie zufrieden waren Sie mit der heutigen Beratung im Allgemeinen?</text>
      <text x="205" y="76">1○   2○   3○   4○   5○   6○   7○   8○   9○   10○</text>
      <text x="205" y="84">Wie wahrscheinlich ist es, dass Sie uns Freunden oder der Familie weiterempfehlen?</text>
      <text x="205" y="89">1○   2○   3○   4○   5○   6○   7○   8○   9○   10○</text>
      <text x="205" y="97">Wie beurteilen Sie die Qualität des Beratungsgesprächs hinsichtlich Klarheit und Verständlichkeit?</text>
      <text x="205" y="102">1○   2○   3○   4○   5○   6○   7○   8○   9○   10○</text>
      <text x="205" y="109">(1 trifft überhaupt nicht zu / 10 trifft voll zu)</text>
      <text x="205" y="134" style="font-size:3px">Empfehlungen / Kontakte</text>
      <text x="205" y="138">Diese Personen könnten ebenfalls interessiert sein</text>
      <text x="205" y="144">Name</text><text x="240" y="144">Adresse</text><text x="293" y="144">Telefonnummer</text>
      <text x="205" y="209" style="font-size:3px">Nächster Termin</text>
      <text x="205" y="219">Thema</text>
      <text x="205" y="232">Ort / Datum</text><text x="292" y="232">Kundenunterschrift</text>
      <text x="205" y="240">Die erhobenen Daten werden für die Beratung und Betreuung verwendet.</text>
      <text x="205" y="244">Sie werden vertraulich behandelt und nicht an Dritte weitergegeben.</text>
    </g>
    <path class="ln" d="M205 151 H232 M240 151 H286 M293 151 H358 M205 159 H232 M240 159 H286 M293 159 H358 M205 167 H232 M240 167 H286 M293 167 H358 M205 175 H232 M240 175 H286 M293 175 H358 M205 183 H232 M240 183 H286 M293 183 H358 M205 191 H232 M240 191 H286 M293 191 H358 M205 222 H358 M205 229 H270 M292 229 H358"/>
    <circle cx="341" cy="253" r="2" fill="var(--teal-dark)"/>
    <text x="344.5" y="254" class="brand">Nordlicht Vorsorge</text>
  </svg>
</div>

<!-- Back cover -->
<div class="sheet back" style="left:956px;top:500px;width:189px;height:266px">
  <svg viewBox="0 0 189 266">
    <rect x="0" y="45" width="189" height="128" fill="url(#sky)" role="img" aria-label="Foto: Holzsteg unter blauem Himmel mit Wolken"/>
    <circle cx="60" cy="210" r="2.5" fill="var(--teal-dark)"/>
    <text x="65" y="212.5" style="font-size:7px;fill:var(--blue)">Nordlicht Vorsorge</text>
    <text x="94.5" y="222" text-anchor="middle" class="lbl" style="fill:var(--blue)">Nordlicht Vorsorge GmbH</text>
    <text x="94.5" y="226" text-anchor="middle" class="lbl" style="fill:var(--blue)">Lindenweg 12</text>
    <text x="94.5" y="230" text-anchor="middle" class="lbl" style="fill:var(--blue)">9000 Talwil</text>
  </svg>
</div>

</div>
</body>
</html>
```